Kestrel Summit 2019 Enemies of the End-Times Church Flyer

We want a church conference flyer designed. We are looking for a professional, yet catchy design that uses our brand colors and logo creatively while communicating key information of the event effectively. <br/>The flyer must include all of the following:<br/>Title: Kestrel Summit 2019<br/>Topic: The Enemies of The End-Times Church <br/>Subtitles: <br/> -How the antichrist raises an army by social behavior engineering. <br/>-How the architects of modern social constructs escaped the church's radar. <br/>-The Holy Spirit's end-times agenda:<br/> The Knock-Out Punch!<br/>Speaker: Prophet Marcus Toliver <br/>Dates/time: December 27, 28 & 29 at 6pm<br/>Location: Halvorn Community Center <br/> 241 Pellham Street <br/> Portland, ME 04102<br/>Contact info: phone: 207-555-0148 <br/>email: contact@brookmeadow.example <br/> www.vutel.example<br/>*The flyer must also include a picture of the speaker and our Vutel logo <br/>Thanks, we look forward to seeing what you come up with!

Colors

Designer to choose colors to be used in the design.

Requirements
Must have
• The flyer must include all of the following:
• Title: Kestrel Summit 2019
• Topic: The Enemies of The End-Times Church
• Subtitles:
• -How the antichrist raises an army by social behavior engineering.
• -How the architects of modern social constructs escaped the church's radar.
• -The Holy Spirit's end-times agenda:
• The Knock-Out Punch!
• Speaker: Prophet Marcus Toliver
• Dates/time: December 27, 28 & 29 at 6pm
• Location: Halvorn Community Center
• 241 Pellham Street
• Portland, ME 04102
• Contact info: phone: 207-555-0148
• email: contact@brookmeadow.example
• www.vutel.example
• *The flyer must also include a picture of the speaker and our Vutel logo
Should not have
• Pictures of crosses or church buildings

```html
<!DOCTYPE html>
<html lang="en">
<head>
<meta charset="utf-8">
<title>Kestrel Summit 2019</title>
<link rel="stylesheet" href="https://fonts.googleapis.com/css2?family=Cinzel:wght@700&family=Libre+Baskerville:wght@700&family=Montserrat:wght@500;600;700;800&family=Open+Sans:wght@700;800&display=swap">
<style>
  :root {
    --navy: #0b3557;
    --night: #031f37;
    --orange: #f7941d;
    --bronze: #b5651d;
    --pill: #eaf5f7;
    --white: #ffffff;
    --mist: #f3f7fa;
  }
  * { margin: 0; padding: 0; box-sizing: border-box; }
  html, body { width: 785px; height: 1200px; overflow: hidden; background: var(--white); }
  .flyer {
    position: relative; width: 785px; height: 1200px; overflow: hidden;
    background: linear-gradient(180deg, var(--mist) 0%, #fbfcfd 45%, var(--white) 100%);
    font-family: "Open Sans", sans-serif;
  }
  .brand {
    position: absolute; top: 50px; left: 0; width: 100%;
    display: flex; justify-content: center; align-items: center; gap: 12px;
  }
  .brand-dot { width: 16px; height: 16px; border-radius: 50%; background: var(--orange); }
  .brand-name {
    font-family: "Cinzel", serif; font-weight: 700; font-size: 42px;
    color: var(--navy); letter-spacing: 1px; line-height: 1;
  }
  .title {
    position: absolute; top: 138px; left: 0; width: 100%; text-align: center;
    font-family: "Cinzel", serif; font-weight: 700; font-size: 48px;
    color: var(--navy); letter-spacing: 1px; line-height: 1;
  }
  .topic {
    position: absolute; top: 201px; left: 0; width: 100%; text-align: center;
    font-family: "Cinzel", serif; font-weight: 700; font-size: 22.5px;
    color: var(--orange); line-height: 1;
  }
  .points {
    position: absolute; top: 272px; left: 90px; width: 630px;
    font-weight: 800; font-size: 18.5px; line-height: 27px;
    color: var(--navy); letter-spacing: 0.6px; list-style: none;
  }
  .agenda {
    position: absolute; right: 43px; top: 400px; text-align: right;
    font-weight: 800; font-size: 27px; line-height: 44px; letter-spacing: 0.5px;
  }
  .agenda .lead { color: var(--navy); display: block; }
  .agenda .punch { color: var(--orange); display: block; }
  .band {
    position: absolute; left: 0; top: 547px; width: 100%; height: 569px;
    background: var(--night);
  }
  .speaker-pill {
    position: absolute; left: 240px; top: 500px; width: 508px; height: 82px;
    background: var(--pill); border: 5px solid var(--orange); border-radius: 22px;
    display: flex; align-items: center; justify-content: center; padding-left: 40px;
    font-family: "Cinzel", serif; font-weight: 700; font-size: 27px;
    color: var(--night); letter-spacing: 1px;
  }
  .speaker-photo {
    position: absolute; left: 40px; top: 428px; width: 226px; height: 226px;
    border-radius: 50%; border: 6px solid var(--orange);
    background: radial-gradient(circle at 45% 40%, #8a6a4c 0%, #a59877 40%, #6b5a44 70%, #b9c6de 100%);
  }
  .dates { position: absolute; left: 0; top: 0; }
  .date-num {
    font-family: "Libre Baskerville", serif; font-weight: 700; font-size: 78px;
    fill: var(--night); letter-spacing: -3px;
  }
  .date-month {
    font-family: "Libre Baskerville", serif; font-weight: 700; font-size: 13.5px;
    fill: var(--bronze);
  }
  .time {
    position: absolute; top: 860px; left: 0; width: 100%; text-align: center;
    font-family: "Montserrat", sans-serif; font-weight: 800; font-size: 37px;
    color: var(--orange); letter-spacing: -0.5px;
    -webkit-text-stroke: 1.2px var(--white); paint-order: stroke fill;
  }
  .venue {
    position: absolute; left: 225px; top: 927px; width: 349px; height: 131px;
    background: var(--white); border: 5px solid var(--orange); border-radius: 10px;
    text-align: center; font-family: "Montserrat", sans-serif; padding-top: 12px;
  }
  .venue-label { font-weight: 700; font-size: 19px; color: var(--orange); letter-spacing: 0.5px; }
  .venue-address { font-weight: 500; font-size: 15px; line-height: 22px; color: var(--night); letter-spacing: 0.4px; margin-top: 2px; }
  .contact {
    position: absolute; left: 0; top: 1116px; width: 100%; height: 84px;
    background: var(--white); font-family: "Montserrat", sans-serif;
    font-weight: 700; font-size: 20px;
  }
  .contact-phone {
    position: absolute; left: 0; top: 0; width: 231px; height: 84px;
    display: flex; align-items: center; justify-content: center; padding-top: 6px;
    color: var(--orange);
  }
  .contact-email {
    position: absolute; left: 231px; top: 0; width: 333px; height: 84px;
    background: var(--orange); color: var(--white); font-size: 17px;
    display: flex; align-items: center; justify-content: center; padding-top: 6px;
    white-space: nowrap;
  }
  .contact-web {
    position: absolute; left: 564px; top: 0; width: 221px; height: 84px;
    display: flex; align-items: center; justify-content: center; padding-top: 2px;
    color: var(--orange); font-size: 17.5px; white-space: nowrap;
  }
</style>
</head>
<body>
<main class="flyer">
  <header class="brand">
    <span class="brand-dot"></span>
    <span class="brand-name">Vutel</span>
  </header>

  <h1 class="title">KESTREL SUMMIT 2019</h1>
  <h2 class="topic">THE ENEMIES OF THE END-TIMES CHURCH</h2>

  <ul class="points">
    <li>How the antichrist raises an army by social behavior engineering.</li>
    <li>How the architects of modern social constructs escaped the church's radar.</li>
  </ul>

  <p class="agenda">
    <span class="lead">The Holy Spirit's end-times agenda:</span>
    <span class="punch">The Knock-Out Punch!</span>
  </p>

  <div class="band"></div>

  <div class="speaker-pill">PROPHET MARCUS TOLIVER</div>
  <div class="speaker-photo" role="img" aria-label="Portrait photo of Prophet Marcus Toliver speaking with a headset microphone"></div>

  <svg class="dates" width="785" height="1200" viewBox="0 0 785 1200" aria-label="December 27, 28 and 29">
    <defs>
      <linearGradient id="silver" x1="0" y1="0" x2="1" y2="1">
        <stop offset="0" stop-color="#ffffff"/>
        <stop offset="0.45" stop-color="#9ea3a8"/>
        <stop offset="0.6" stop-color="#eef0f2"/>
        <stop offset="1" stop-color="#8d9297"/>
      </linearGradient>
      <radialGradient id="face" cx="0.45" cy="0.4" r="0.7">
        <stop offset="0" stop-color="#ffffff"/>
        <stop offset="0.7" stop-color="#e6e8ea"/>
        <stop offset="1" stop-color="#c4c8cc"/>
      </radialGradient>
    </defs>
    <g transform="translate(219 774)">
      <circle r="78" fill="url(#silver)"/><circle r="70" fill="var(--night)"/><circle r="63" fill="url(#face)"/>
      <text class="date-num" text-anchor="middle" y="22">27</text>
      <text class="date-month" text-anchor="middle" y="40">DECEMBER</text>
    </g>
    <g transform="translate(403 774)">
      <circle r="78" fill="url(#silver)"/><circle r="70" fill="var(--night)"/><circle r="63" fill="url(#face)"/>
      <text class="date-num" text-anchor="middle" y="22">28</text>
      <text class="date-month" text-anchor="middle" y="40">DECEMBER</text>
    </g>
    <g transform="translate(610 774)">
      <circle r="78" fill="url(#silver)"/><circle r="70" fill="var(--night)"/><circle r="63" fill="url(#face)"/>
      <text class="date-num" text-anchor="middle" y="22">29</text>
      <text class="date-month" text-anchor="middle" y="40">DECEMBER</text>
    </g>
  </svg>

  <p class="time">FROM 6:00 P.M</p>

  <section class="venue">
    <p class="venue-label">LOCATION</p>
    <p class="venue-address">HALVORN COMMUNITY CENTER,<br>241 PELLHAM STREET,PORTLAND,<br>ME 04102</p>
  </section>

  <footer class="contact">
    <span class="contact-phone">207-555-0148</span>
    <span class="contact-email">contact@brookmeadow.example</span>
    <span class="contact-web">www.vutel.example</span>
  </footer>
</main>
</body>
</html>
```